User-interface and web design for new forum-style communication platform

We developed a new forum-style communication platform specially targetting stock investors to share and discuss information on companies listed on the stock exchange.

You have complete freedom for designing the user-interface and web design. Designs should include all features listed below.

Please read the attached document for full specifications. Also attached is a mockup of the layout, but this is only directional. A mockup for the user-profile is also attached, but does not need to be designed.

This project focusses on the homepage and thread view.

The winner(s) will be asked to design the complete project. (create thread box, user profile, registering, settings...)

We are looking for a well thought out, smart design that incorporates the specifications in the attached document. Please do not hesitate to contact us if anything is not clear.

Target Market(s)

Stock investors from 25 to 60 years old (the people that are currently on investor forums)

Industry/Entity Type

Communication

Font styles to use
Sans Serif

Colors

Designer to choose colors to be used in the design.

Requirements
Must have
• Full homepage design & Thread view specified in the attached document.
Nice to have
• Create thread view
- Field for adding tags
- field for subject of the thread
- text box with basic text editing
- method for sharing media
Should not have
• Logo design.

```html
<!DOCTYPE html>
<html lang="en">
<head>
<meta charset="utf-8">
<title>Quorvo – Public Conversations</title>
<link href="https://fonts.googleapis.com/css2?family=Open+Sans:wght@400;600;700&display=swap" rel="stylesheet">
<style>
:root{
  --teal:#1bb394;
  --teal-dark:#13917a;
  --bg:#ebeeee;
  --white:#ffffff;
  --ink:#1e1e1e;
  --muted:#7a7a7a;
  --line:#d2d4d4;
  --panel-soft:#f1f1f1;
  --page-chip:#c9cccc;
}
*{box-sizing:border-box;margin:0;padding:0}
html,body{width:858px;height:1200px;overflow:hidden}
body{position:relative;background:var(--bg);font-family:'Open Sans',sans-serif;color:var(--ink)}
.abs{position:absolute}

/* header */
.site-header{left:0;top:0;width:858px;height:72px;background:var(--white);border-bottom:1px solid #bfc2c2}
.brand{left:130px;top:24px;font-weight:700;font-size:22px;letter-spacing:.5px;color:#111}
.search-bar{left:276px;top:22px;width:214px;height:32px;border:1px solid var(--line);border-radius:16px 0 0 16px;background:#f1f2f2}
.search-bar svg{position:absolute;left:12px;top:8px}
.search-bar span{position:absolute;left:32px;top:8px;font-size:10px;color:#9a9a9a}
.btn-save{left:490px;top:22px;width:53px;height:32px;background:var(--teal);color:#fff;font-size:10px;text-align:center;line-height:32px}
.btn-clear{left:543px;top:22px;width:54px;height:32px;background:#121212;color:#fff;font-size:10px;text-align:center;line-height:32px}
.notif-icon{left:643px;top:36px}
.notif-badge{left:651px;top:33px;width:14px;height:12px;border-radius:7px;background:var(--teal);color:#fff;font-size:7px;text-align:center;line-height:12px}
.tooltip{left:610px;top:56px;width:79px;height:27px;background:#f7f7f7;border:1px solid #ddd;box-shadow:0 2px 4px rgba(0,0,0,.18);font-size:8.5px;text-align:center;line-height:27px}
.tooltip::before{content:"";position:absolute;left:36px;top:-5px;width:8px;height:8px;background:#f7f7f7;border-left:1px solid #ddd;border-top:1px solid #ddd;transform:rotate(45deg)}
.avatar-me{left:693px;top:27px;width:22px;height:22px;border-radius:50%;background:linear-gradient(135deg,#c99a7b,#6b4a3c)}
.online-dot{left:709px;top:27px;width:6px;height:6px;border-radius:50%;background:#3ccf6e}
.caret{left:724px;top:36px;border-left:3px solid transparent;border-right:3px solid transparent;border-top:4px solid #333}

/* sidebar */
.panel{background:var(--white);left:123px;width:195px}
.panel-head{height:37px;background:linear-gradient(#fff,#e6e6e6);color:var(--teal);font-weight:700;font-size:12px;padding:13px 7px 0}
.user-search{position:absolute;left:6px;top:63px;width:172px;height:30px;border:1px solid var(--line);background:#f3f3f3;border-radius:2px}
.user-search svg{position:absolute;left:9px;top:9px}
.user-search span{position:absolute;left:24px;top:8px;font-size:9px;color:#9a9a9a}
.check-list{position:absolute;left:7px;width:171px;background:var(--panel-soft);list-style:none;padding-top:11px}
.check-list li{height:20.2px;font-size:9px;color:#333;padding-left:34px;position:relative}
.check-list li::before{content:"";position:absolute;left:22px;top:3px;width:7px;height:7px;background:#777}
.check-list li::after{content:"";position:absolute;left:24px;top:4px;width:2px;height:4px;border:solid #fff;border-width:0 1px 1px 0;transform:rotate(45deg)}
.show-all{position:absolute;left:13px;font-size:9px;color:var(--teal);text-decoration:underline}

/* main */
.crumbs{left:334px;top:124px;font-size:10px;color:var(--teal);font-weight:600}
.crumbs .sep{color:#555;margin:0 6px}
.crumbs .current{color:#555}
.tabs{left:327px;top:158px;width:409px;height:30px;background:var(--teal)}
.tab{position:absolute;top:0;height:30px;line-height:30px;color:#fff;font-size:9.5px}
.tab-active{left:0;width:51px;background:var(--teal-dark);text-align:center}
.tab-active::after{content:"";position:absolute;left:22px;bottom:-1px;border-left:5px solid transparent;border-right:5px solid transparent;border-bottom:5px solid #f7f7f7}
.create-thread{position:absolute;left:326px;top:7px;width:76px;height:19px;background:#fff;color:var(--teal);font-size:8.5px;text-align:center;line-height:19px;border-radius:1px}
.menu{background:#f7f7f7;border:1px solid #ddd;box-shadow:0 2px 5px rgba(0,0,0,.18);list-style:none;font-size:8.5px;padding:11px 0 0 20px;z-index:2}
.menu li{height:15px;position:relative}
.menu li::before{content:"";position:absolute;left:-8px;top:5px;width:3px;height:3px;border-radius:50%;background:#111}

.post{left:327px;width:409px;height:179px;background:var(--white)}
.thumb{position:absolute;left:10px;top:22px;width:46px;height:30px}
.post-title{position:absolute;left:70px;top:19px;font-size:9px}
.meta{position:absolute;left:70px;top:40px;font-size:7.5px;color:var(--muted);display:flex;gap:20px}
.meta span{display:flex;align-items:center;gap:5px}
.post-body{position:absolute;left:70px;top:62px;width:330px;font-size:8px;line-height:14.6px;color:#444}
.post-actions{position:absolute;left:0;top:138px;width:409px;height:26px}
.read-more{position:absolute;left:22px;top:7px;font-size:8px;color:var(--teal);font-weight:600}
.stat{position:absolute;top:8px;font-size:7.5px;color:var(--muted);display:flex;align-items:center;gap:4px}
.action{position:absolute;top:0;width:58px;height:26px;background:var(--teal);color:#fff;font-size:8.5px;text-align:center;line-height:26px}

.comment-avatar{left:327px;width:44px;height:38px;border:1px solid #ddd}
.comment-box{left:391px;width:345px;height:49px;background:var(--white);border:1px solid #ccc;font-size:7px;color:#888;padding:7px 8px}

/* pagination */
.pager{left:0;top:1073px;width:858px;height:14px}
.pg{position:absolute;top:0;width:14px;height:14px;background:var(--page-chip);color:#fff;font-size:7.5px;text-align:center;line-height:14px}
.pg.on{background:#fff;color:#111}
.pg.dark{background:#9ea1a1}

/* footer */
.site-footer{left:0;top:1126px;width:858px;height:54px;background:var(--white);border-top:1px solid #ddd}
.copyright{position:absolute;left:130px;top:22px;font-size:9px;color:#444}
.social{position:absolute;top:23px;width:9px;height:9px;border-radius:2px;background:#a5a8a8}
.bottom-strip{left:0;top:1180px;width:858px;height:20px;background:#e3e5e5;border-top:1px solid #ccc}
</style>
</head>
<body>

<header class="abs site-header"></header>
<div class="abs brand">Quorvo</div>
<div class="abs search-bar">
  <svg width="14" height="14" viewBox="0 0 14 14"><circle cx="6" cy="6" r="4.5" fill="none" stroke="#888" stroke-width="1.6"/><line x1="9.3" y1="9.3" x2="13" y2="13" stroke="#888" stroke-width="1.8"/></svg>
  <span>#northwind #acmecorp</span>
</div>
<div class="abs btn-save">Save</div>
<div class="abs btn-clear">Clear</div>
<svg class="abs notif-icon" width="12" height="12" viewBox="0 0 12 12" fill="#555">
  <rect x="0" y="0" width="3" height="3"/><rect x="4.5" y="0" width="3" height="3"/><rect x="9" y="0" width="3" height="3"/>
  <rect x="0" y="4.5" width="3" height="3"/><rect x="4.5" y="4.5" width="3" height="3"/><rect x="9" y="4.5" width="3" height="3"/>
  <rect x="0" y="9" width="3" height="3"/><rect x="4.5" y="9" width="3" height="3"/><rect x="9" y="9" width="3" height="3"/>
</svg>
<div class="abs notif-badge">3</div>
<div class="abs tooltip">1 New Follower</div>
<div class="abs avatar-me" role="img" aria-label="Signed-in user profile photo"></div>
<div class="abs online-dot"></div>
<div class="abs caret"></div>

<!-- sidebar -->
<section class="abs panel" style="top:114px;height:118px">
  <div class="panel-head">Users</div>
  <div class="user-search">
    <svg width="11" height="11" viewBox="0 0 14 14"><circle cx="6" cy="6" r="4.5" fill="none" stroke="#888" stroke-width="1.8"/><line x1="9.3" y1="9.3" x2="13" y2="13" stroke="#888" stroke-width="2"/></svg>
    <span>Search</span>
  </div>
</section>

<section class="abs panel" style="top:248px;height:240px">
  <div class="panel-head">Saved Filters</div>
  <ul class="check-list" style="top:64px;height:136px">
    <li>Item one</li><li>Item Two</li><li>Item Three</li><li>Item one</li><li>Item Two</li><li>Item Three</li>
  </ul>
  <span class="show-all" style="top:213px">Show All</span>
</section>

<section class="abs panel" style="top:506px;height:240px">
  <div class="panel-head">Popular Tags</div>
  <ul class="check-list" style="top:64px;height:136px">
    <li>Item one</li><li>Item Two</li><li>Item Three</li><li>Item one</li><li>Item Two</li><li>Item Three</li>
  </ul>
  <span class="show-all" style="top:213px">Show All</span>
</section>

<section class="abs panel" style="top:763px;height:184px">
  <div class="panel-head">Popular Contributors</div>
  <ul class="check-list" style="top:63px;height:77px">
    <li>Item one</li><li>Item Two</li><li>Item Three</li>
  </ul>
  <span class="show-all" style="top:157px">Show All</span>
</section>

<!-- main -->
<nav class="abs crumbs">Home<span class="sep">›</span>Conversations<span class="sep">›</span>Public<span class="sep">›</span><span class="current">#northwind #acmecorp</span></nav>

<div class="abs tabs">
  <div class="tab tab-active">Public</div>
  <div class="tab" style="left:64px">Following</div>
  <div class="tab" style="left:129px">Contacts</div>
  <div class="create-thread">Create Thread</div>
</div>

<!-- post template repeated -->
<article class="abs post" style="top:213px">
  <div class="thumb" role="img" aria-label="Thread thumbnail: chart and report illustration" style="background:linear-gradient(135deg,#5b8fd6,#d94a3a)"></div>
  <div class="post-title">Lorem ipsum dolor sit amet, consectetuer adipiscing elit.</div>
  <div class="meta">
    <span><svg width="8" height="9" viewBox="0 0 8 9" fill="#999"><circle cx="4" cy="2.3" r="2.2"/><path d="M0 9c0-3 1.8-4.3 4-4.3S8 6 8 9z"/></svg>Daniel Hart</span>
    <span><svg width="9" height="9" viewBox="0 0 9 9" fill="#999"><rect x="0" y="1" width="9" height="8" rx="1"/><rect x="1" y="3.5" width="7" height="4.5" fill="#fff"/></svg>12.56 - Mar 31,2014</span>
  </div>
  <p class="post-body">Lorem ipsum dolor sit amet, consectetuer adipiscing elit. Nam cursus. Morbi ut mi. Nullam enim leo, egestas id, condimentum at, laoreet mattis, massa. Sed eleifend nonummy diam. Praesent mauris ante, elementum et, bibendum at, posuere sit amet, nibh.Lorem ipsum dolor sit amet, consectetuer adipiscing elit.</p>
  <div class="post-actions">
    <span class="read-more">READ MORE</span>
    <span class="stat" style="left:85px"><svg width="9" height="7" viewBox="0 0 9 7" fill="#999"><path d="M3.5 0L0 3l3.5 3V4.2c2.5 0 4 .6 5.5 2.8C8.5 3.8 6.8 2 3.5 1.8z"/></svg>12 replies</span>
    <span class="stat" style="left:143px"><svg width="11" height="7" viewBox="0 0 11 7"><path d="M0 3.5C2 0 9 0 11 3.5 9 7 2 7 0 3.5z" fill="#999"/><circle cx="5.5" cy="3.5" r="1.6" fill="#fff"/></svg>127 Views</span>
    <span class="action" style="left:205px">Reply</span>
    <span class="action" style="left:273px">Share</span>
    <span class="action" style="left:341px">Favorite</span>
  </div>
</article>
<div class="abs comment-avatar" style="top:415px" role="img" aria-label="Commenter avatar" ></div>
<div class="abs comment-box" style="top:415px">Write a Comment..</div>

<article class="abs post" style="top:494px">
  <div class="thumb" role="img" aria-label="Thread thumbnail: photo" style="background:linear-gradient(135deg,#d8b8a0,#8a5a44)"></div>
  <div class="post-title">Lorem ipsum dolor sit amet, consectetuer adipiscing elit.</div>
  <div class="meta">
    <span><svg width="8" height="9" viewBox="0 0 8 9" fill="#999"><circle cx="4" cy="2.3" r="2.2"/><path d="M0 9c0-3 1.8-4.3 4-4.3S8 6 8 9z"/></svg>Daniel Hart</span>
    <span><svg width="9" height="9" viewBox="0 0 9 9" fill="#999"><rect x="0" y="1" width="9" height="8" rx="1"/><rect x="1" y="3.5" width="7" height="4.5" fill="#fff"/></svg>12.56 - Mar 31,2014</span>
  </div>
  <p class="post-body">Lorem ipsum dolor sit amet, consectetuer adipiscing elit. Nam cursus. Morbi ut mi. Nullam enim leo, egestas id, condimentum at, laoreet mattis, massa. Sed eleifend nonummy diam. Praesent mauris ante, elementum et, bibendum at, posuere sit amet, nibh.Lorem ipsum dolor sit amet, consectetuer adipiscing elit.</p>
  <div class="post-actions">
    <span class="read-more">READ MORE</span>
    <span class="stat" style="left:85px"><svg width="9" height="7" viewBox="0 0 9 7" fill="#999"><path d="M3.5 0L0 3l3.5 3V4.2c2.5 0 4 .6 5.5 2.8C8.5 3.8 6.8 2 3.5 1.8z"/></svg>12 replies</span>
    <span class="stat" style="left:143px"><svg width="11" height="7" viewBox="0 0 11 7"><path d="M0 3.5C2 0 9 0 11 3.5 9 7 2 7 0 3.5z" fill="#999"/><circle cx="5.5" cy="3.5" r="1.6" fill="#fff"/></svg>127 Views</span>
    <span class="action" style="left:205px">Reply</span>
    <span class="action" style="left:273px">Share</span>
    <span class="action" style="left:341px">Favorite</span>
  </div>
</article>
<div class="abs comment-avatar" style="top:698px" role="img" aria-label="Commenter avatar"></div>
<div class="abs comment-box" style="top:698px">Write a Comment..</div>

<article class="abs post" style="top:776px">
  <div class="thumb" role="img" aria-label="Thread thumbnail: author avatar" style="background:linear-gradient(135deg,#2f6fd0,#f2b13a)"></div>
  <div class="post-title">Lorem ipsum dolor sit amet, consectetuer adipiscing elit.</div>
  <div class="meta">
    <span><svg width="8" height="9" viewBox="0 0 8 9" fill="#999"><circle cx="4" cy="2.3" r="2.2"/><path d="M0 9c0-3 1.8-4.3 4-4.3S8 6 8 9z"/></svg>Daniel Hart</span>
    <span><svg width="9" height="9" viewBox="0 0 9 9" fill="#999"><rect x="0" y="1" width="9" height="8" rx="1"/><rect x="1" y="3.5" width="7" height="4.5" fill="#fff"/></svg>12.56 - Mar 31,2014</span>
  </div>
  <p class="post-body">Lorem ipsum dolor sit amet, consectetuer adipiscing elit. Nam cursus. Morbi ut mi. Nullam enim leo, egestas id, condimentum at, laoreet mattis, massa. Sed eleifend nonummy diam. Praesent mauris ante, elementum et, bibendum at, posuere sit amet, nibh.Lorem ipsum dolor sit amet, consectetuer adipiscing elit.</p>
  <div class="post-actions">
    <span class="read-more">READ MORE</span>
    <span class="stat" style="left:85px"><svg width="9" height="7" viewBox="0 0 9 7" fill="#999"><path d="M3.5 0L0 3l3.5 3V4.2c2.5 0 4 .6 5.5 2.8C8.5 3.8 6.8 2 3.5 1.8z"/></svg>12 replies</span>
    <span class="stat" style="left:143px"><svg width="11" height="7" viewBox="0 0 11 7"><path d="M0 3.5C2 0 9 0 11 3.5 9 7 2 7 0 3.5z" fill="#999"/><circle cx="5.5" cy="3.5" r="1.6" fill="#fff"/></svg>127 Views</span>
    <span class="action" style="left:205px">Reply</span>
    <span class="action" style="left:273px">Share</span>
    <span class="action" style="left:341px">Favorite</span>
  </div>
</article>
<div class="abs comment-avatar" style="top:979px" role="img" aria-label="Commenter avatar"></div>
<div class="abs comment-box" style="top:979px">Write a Comment..</div>

<ul class="abs menu" style="left:313px;top:190px;width:79px;height:48px">
  <li>Recent</li><li>Popular</li>
</ul>
<ul class="abs menu" style="left:319px;top:830px;width:79px;height:48px">
  <li>View Profile</li><li>View All Posts</li>
</ul>

<!-- pagination -->
<div class="abs pager">
  <svg class="abs" style="left:327px;top:3px" width="6" height="9" viewBox="0 0 6 9"><path d="M5 0.5L1 4.5 5 8.5" fill="none" stroke="#bbb" stroke-width="1.2"/></svg>
  <span class="pg" style="left:349px">1</span>
  <span class="pg" style="left:376px">2</span>
  <span class="pg" style="left:403px">3</span>
  <span class="pg" style="left:430px">4</span>
  <span class="pg" style="left:457px">5</span>
  <span class="pg" style="left:484px">6</span>
  <span class="pg on" style="left:511px">7</span>
  <span class="pg" style="left:538px">8</span>
  <span class="pg dark" style="left:565px">9</span>
  <span class="pg" style="left:592px">10</span>
  <span class="pg" style="left:619px">11</span>
  <span class="pg" style="left:646px;width:41px">1586</span>
  <svg class="abs" style="left:702px;top:3px" width="6" height="9" viewBox="0 0 6 9"><path d="M1 0.5L5 4.5 1 8.5" fill="none" stroke="#666" stroke-width="1.2"/></svg>
</div>

<footer class="abs site-footer">
  <span class="copyright">Copyright © 2014 - All Rights Reserved</span>
  <span class="social" style="left:618px"></span>
  <span class="social" style="left:637px"></span>
  <span class="social" style="left:656px"></span>
  <span class="social" style="left:676px"></span>
  <span class="social" style="left:696px"></span>
  <span class="social" style="left:715px"></span>
</footer>
<div class="abs bottom-strip"></div>

</body>
</html>
```